German CBD company needs a label+packaging design (templates provided)

Hey there,
we are a German e-commerce company and about to launch a CBD E-liquid series under our new brand "VELMORIQ". We need designs for the cardbord tube packaging and the labels of bottles. Find attached templates for both, the labels and the packaging. The templates already have a design on them just for you to know that some space will be filled with legal information. Feel free to use the templates and change the designs and of course we have the suitable text down below. Every outer packaging label and bottle label should include the brand name "VELMORIQ" (we typically use the font Archivo Black, but feel free to change it, if you have a better idea), the CBD content, the flavour and the filling quantity (10ml). You can use 100mg and Mango for your design and if your design wins, we will work with you and change the flavours and concentrations for the other liquids accordingly. Our liquids are Made in Germany and of a very high quality so we are looking for a premium design that underlines the quality und purity of our product. Something between luxurious and futuristic. Please let your creativity run wild :)

As for the packaging we need the following texts on the packaging:

DE:
(bold)Inhaltsstoffe:(bold) < 70% Propylen Glycol, < 30% VG Glycerol, Aromen, Cannabidiol (CBD) wie angegeben CAS 13956-29-1.
(bold)Anwendung(bold) Vor Benutzung schütteln. Dieses Produkt ist unverdünnt in einer kompatiblen e-Zigarette anzuwenden. 2-3 Züge inhalieren. Zwischen den Anwendungen 10-20 Minuten warten. Dieses Produkt ersetzt keine ausgewogene Ernährung.
(bold)Hinweise:(bold) VELMORIQ CBD e-Liquids sind Tabakersatzprodukte gem. TPD2 und bestehen aus organischen und zertifizierten, >99% reinen CBD-Kristallen. HACCP & GMP konform. Nicht empfohlen für Schwangere, stillende Frauen oder Nichtraucher. Dieses Produkt ist nicht zur Diagnose, Behandlung, Heilung oder Vorbeugung von Krankheiten bestimmt. Darf nicht in die Hände von Kindern und Jugendlichen gelangen. Keine Abgabe unter 18 Jahren. Dunkel und kühl lagern. Nicht zum Verzehr geeignet.

EN:
(bold)Ingredients:(bold) < 70% Propylen Glycol, < 30% VG Glycerol, flavours , Cannabidiol (CBD).
(bold)Application(bold): Shake before use. This product should be applied undiluted in a compatible e-cigarette. Inhale 2-3 puffs. Wait 10-20 minutes until using again.
(bold)Notes(bold): VELMORIQ e-liquids are made from organic and certified >99% pure CBD Crystals. HACCP & GMP compliant. Not recommended for pregnant or breastfeeding women or non-smokers.
This product is not intended to diagnose, treat, cure or prevent any disease. Keep away from children. No sale to minors. Store in a cool, dark place. Not for consumption.

DE: Qualität:
Wir verwenden für unsere Liquids organische und zertifizierte CBD-Kristalle von >99% Reinheit. Wir verwenden nur die hochwertigsten Rohstoffe zur Herstellung unserer Liquids, um unseren Kunden ein optimales Vape-Erlebnis bieten zu können.
EN: Quality:
We use organic and certified CBD-Crystals with a purity >99%. We only use the highest quality raw material for the production of our liquids in order to ensure an optimal vaping experience for our customers.

Please consider that we will also need space for our contact information, our website URL and an EAN bar code.

Now the label for the bottles: As already said our templates have designs on them, so please feel free to change anything you like. It`s just an example of the label printing company so we could get an idea. We just need the following texts on those labels:
DE:(bold)Inhaltsstoffe:(bold) < 70% Propylen Glycol, < 30% VG Glycerol, Aromen, Cannabidiol (CBD) wie angegeben CAS 13956-29-1.
Darf nicht in die Hände von Kindern und Jugendlichen gelangen. Keine Abgabe unter 18 Jahren.

EN:(bold)Ingredients:(bold) < 70% Propylen Glycol, < 30% VG Glycerol, flavours , Cannabidiol (CBD).
Keep away from children. No sale to minors.
Moreover, we need the symbols that are already on the label and some space for an EAN bar code. The labels should include CBD content, brand name, flavour..(see above)

I hope our briefing is clear enough. If you have any further questions, please contact me via e-mail (olek.dravin@quenlo-shop.example).
We are looking forwards to receiving your designs and doing some further work with you. We know that it`s more than one simple task, so we are willing to pay a little bonus for the further work which we will do with the winner :)

Greetings from Frankfurt, Germany
Quenlo GmbH Team
Olek Dravin
olek.dravin@quenlo-shop.example

Font styles to use
Other font styles liked:
• Archivo Black (not mandatory, just an idea)

Colors

Designer to choose colors to be used in the design.

Requirements
Must have
• - Legal notices as mentioned above
• - CBD content in mg
• - flavour
• - space for EAN bar code & contact information
Should not have
• - shouldn`t look too clean, not like a medicine

```html
<!DOCTYPE html>
<html lang="en">
<head>
<meta charset="utf-8">
<title>VELMORIQ CBD E-Liquid – Labels &amp; Tubes</title>
<link rel="stylesheet" href="https://fonts.googleapis.com/css2?family=Archivo+Black&family=Fira+Sans+Condensed:wght@600;700&family=Fira+Sans:ital,wght@0,600;1,600&display=swap">
<style>
  :root {
    --page: #ffffff;
    --stage: #e7e7e7;
    --label: #ffffff;
    --ink: #141414;
    --ink-soft: #6f6f6f;
    --mango: #c9ad2e;
    --melon: #9b2c4c;
  }
  * { box-sizing: border-box; margin: 0; padding: 0; }
  html, body { width: 927px; height: 1200px; overflow: hidden; background: var(--page); }
  body { position: relative; font-family: "Fira Sans Condensed", sans-serif; color: var(--ink); }

  .stage {
    position: absolute;
    width: 358px;
    background: var(--stage);
    display: flex;
    align-items: center;
    justify-content: center;
  }
  .stage--bottle { top: 120px; height: 437px; }
  .stage--tube { top: 599px; height: 476px; }
  .stage--left { left: 93px; }
  .stage--right { left: 469px; }

  .flavour-mango { --flavour: var(--mango); }
  .flavour-melon { --flavour: var(--melon); }

  .label {
    position: relative;
    background: var(--label);
    overflow: hidden;
  }
  .label--bottle { width: 210px; height: 330px; }
  .label--tube { width: 270px; height: 440px; }

  .brand {
    position: absolute;
    left: 0; right: 0;
    text-align: center;
    font-family: "Archivo Black", sans-serif;
    letter-spacing: 0.06em;
    color: var(--ink);
  }
  .label--bottle .brand { top: 40px; font-size: 27px; }
  .label--tube .brand { top: 38px; font-size: 33px; }

  .specs {
    position: absolute;
    left: 14px; right: 10px;
    font-weight: 700;
    letter-spacing: 0.1em;
    text-transform: uppercase;
  }
  .label--bottle .specs { top: 104px; font-size: 11px; line-height: 17px; }
  .label--tube .specs { top: 112px; font-size: 13px; line-height: 20px; }
  .specs__row { display: flex; justify-content: space-between; }
  .specs__amount { border-bottom: 2px solid var(--flavour); }
  .specs__right { color: var(--ink-soft); }
  .label--tube .specs__right { color: var(--ink); }

  .flavour-word {
    position: absolute;
    left: 0; right: 0;
    display: flex;
    flex-direction: column;
    align-items: center;
    justify-content: center;
    font-family: "Fira Sans Condensed", sans-serif;
    font-weight: 700;
    text-transform: uppercase;
    color: var(--flavour);
    line-height: 1;
  }
  .label--bottle .flavour-word { top: 168px; height: 100px; font-size: 32px; letter-spacing: 0.22em; gap: 4px; }
  .label--tube .flavour-word { top: 182px; height: 88px; font-size: 40px; letter-spacing: 0.22em; gap: 4px; }
  .label--bottle .flavour-word--stacked { font-size: 28px; }
  .label--tube .flavour-word--stacked { font-size: 34px; }
  .flavour-word span { padding-left: 0.22em; }

  .flavour-name {
    position: absolute;
    left: 0; right: 0;
    text-align: center;
    font-weight: 600;
    letter-spacing: 0.12em;
    color: var(--flavour);
    text-transform: uppercase;
    white-space: nowrap;
  }
  .label--bottle .flavour-name { top: 282px; font-size: 11px; }
  .label--tube .flavour-name { top: 280px; font-size: 11px; }
  .flavour-rule {
    position: absolute;
    left: 10px; right: 10px; top: 302px;
    height: 2px;
    background: var(--flavour);
  }

  .band {
    position: absolute;
    left: 0; right: 0; bottom: 0;
    height: 138px;
    background: var(--flavour);
    display: flex;
    justify-content: space-between;
    padding: 16px 14px;
    color: var(--label);
    font-family: "Fira Sans", sans-serif;
    font-weight: 600;
    font-size: 8.4px;
    line-height: 11px;
  }
  .band__col { width: 46%; }
  .band__col--en { font-style: italic; text-align: right; }
</style>
</head>
<body>

<!-- Bottle label: Mango -->
<section class="stage stage--bottle stage--left">
  <div class="label label--bottle flavour-mango">
    <h1 class="brand">VELMORIQ</h1>
    <div class="specs">
      <div class="specs__row"><span class="specs__amount">100 MG</span><span>CBD E-Liquid</span></div>
      <div class="specs__row"><span>99% Pure</span><span class="specs__right">Organic</span></div>
      <div class="specs__row"><span>15 ML</span><span class="specs__right">0.5 FL OZ</span></div>
    </div>
    <div class="flavour-word"><span>Mango</span></div>
    <p class="flavour-name">Mango</p>
    <div class="flavour-rule"></div>
  </div>
</section>

<!-- Bottle label: Watermelon -->
<section class="stage stage--bottle stage--right">
  <div class="label label--bottle flavour-melon">
    <h1 class="brand">VELMORIQ</h1>
    <div class="specs">
      <div class="specs__row"><span class="specs__amount">100 MG</span><span>CBD E-Liquid</span></div>
      <div class="specs__row"><span>99% Pure</span><span class="specs__right">Organic</span></div>
      <div class="specs__row"><span>15 ML</span><span class="specs__right">0.5 FL OZ</span></div>
    </div>
    <div class="flavour-word flavour-word--stacked"><span>Water</span><span>Melon</span></div>
    <p class="flavour-name">Watermelon / Wassermelone</p>
    <div class="flavour-rule"></div>
  </div>
</section>

<!-- Tube wrap: Mango -->
<section class="stage stage--tube stage--left">
  <div class="label label--tube flavour-mango">
    <h1 class="brand">VELMORIQ</h1>
    <div class="specs">
      <div class="specs__row"><span class="specs__amount">100 MG</span><span>CBD E-Liquid</span></div>
      <div class="specs__row"><span>99% Pure</span><span class="specs__right">Organic</span></div>
      <div class="specs__row"><span>15 ML</span><span class="specs__right">0.5 FL OZ</span></div>
    </div>
    <div class="flavour-word"><span>Mango</span></div>
    <p class="flavour-name">Mango</p>
    <div class="band">
      <p class="band__col">Wir verwenden für unsere Liquids organische und zertifizierte CBD-Kristalle von &gt;99% Reinheit. Wir verwenden nur die hochwertigsten Rohstoffe zur Herstellung unserer Liquids, um unseren Kunden ein optimales Vape-Erlebnis bieten zu können.</p>
      <p class="band__col band__col--en">We use organic and certified CBD-Crystals with a purity &gt;99%. We only use the highest quality raw material for the production of our liquids in order to ensure an optimal vaping experience for our customers.</p>
    </div>
  </div>
</section>

<!-- Tube wrap: Watermelon -->
<section class="stage stage--tube stage--right">
  <div class="label label--tube flavour-melon">
    <h1 class="brand">VELMORIQ</h1>
    <div class="specs">
      <div class="specs__row"><span class="specs__amount">100 MG</span><span>CBD E-Liquid</span></div>
      <div class="specs__row"><span>99% Pure</span><span class="specs__right">Organic</span></div>
      <div class="specs__row"><span>15 ML</span><span class="specs__right">0.5 FL OZ</span></div>
    </div>
    <div class="flavour-word flavour-word--stacked"><span>Water</span><span>Melon</span></div>
    <p class="flavour-name">Watermelon / Wassermelone</p>
    <div class="band">
      <p class="band__col">Wir verwenden für unsere Liquids organische und zertifizierte CBD-Kristalle von &gt;99% Reinheit. Wir verwenden nur die hochwertigsten Rohstoffe zur Herstellung unserer Liquids, um unseren Kunden ein optimales Vape-Erlebnis bieten zu können.</p>
      <p class="band__col band__col--en">We use organic and certified CBD-Crystals with a purity &gt;99%. We only use the highest quality raw material for the production of our liquids in order to ensure an optimal vaping experience for our customers.</p>
    </div>
  </div>
</section>

</body>
</html>
```